Flyer Dachdeckerhandwerk
Zielgruppe
Die Steilhang- und Kieselwerk GmbH ist ein renommiertes, inhabergeführtes Familienunternehmen im Dachdeckerhandwerk. Seit über 30 Jahren stehen wir für höchste Qualität, Zuverlässigkeit und fachgerechte Ausführung – von der ersten Beratung bis zur termintreuen Umsetzung auf der Baustelle. Unsere Kunden profitieren von fundiertem Know-how, eingespielten Abläufen und einem starken Team, das langlebige und wirtschaftliche Lösungen realisiert.
Wir bieten eine begrenzte Aktion an und bieten bis 30.06.2026 eine kostenfreie Dachinspektion.
Die Kunden sollen hierfür bei uns anrufen, oder eine Mail mit dem Betreff 'Dachinspektion 2026' senden.
Aufgabenstellung
Unser CI laden wir hoch.
Es soll modern aussehen.

```html
<!DOCTYPE html>
<html lang="de">
<head>
<meta charset="utf-8">
<title>Flyer – Steilhang- und Kieselwerk GmbH</title>
<link rel="stylesheet" href="https://fonts.googleapis.com/css2?family=Poppins:wght@400;500;600;700;800&display=swap">
<style>
  :root{
    --stage:#9a9a9a;
    --paper:#f3f3f3;
    --green:#1f9a47;
    --deep-green:#0d4430;
    --charcoal:#333333;
    --text:#3a3a3a;
    --panel:#e4e4e4;
    --bullet:#8c8c8c;
  }
  html,body{margin:0;padding:0;width:765px;height:1200px;overflow:hidden;background:var(--stage);}
  body{position:relative;font-family:"Poppins",sans-serif;}
  .flyer-page{position:absolute;top:353px;width:348px;height:493px;box-shadow:0 6px 14px rgba(0,0,0,.28);background:var(--paper);}
  .flyer-page svg{display:block;width:100%;height:100%;}
  .flyer-front{left:22px;}
  .flyer-back{left:395px;}
  text{font-family:"Poppins",sans-serif;}
  .headline-kicker{font-weight:800;font-size:26px;fill:var(--charcoal);}
  .headline-main{font-weight:800;font-size:42px;fill:var(--green);}
  .headline-sub{font-weight:400;font-size:17px;fill:var(--charcoal);}
  .section-title{font-weight:700;font-size:30px;fill:var(--green);}
  .body-copy{font-size:10.5px;fill:var(--text);}
  .contact-line{font-size:14px;fill:var(--charcoal);}
  .brand-name{font-weight:500;font-size:15px;fill:#ffffff;}
  .services-title{font-weight:700;font-size:30px;fill:var(--deep-green);}
  .service-label{font-weight:600;font-size:11px;fill:#222;}
  .brand-name-green{font-weight:500;font-size:17px;fill:var(--green);}
  .side-title{font-weight:700;font-size:19px;fill:var(--deep-green);}
  .side-copy{font-size:11px;fill:var(--text);}
  .offer-copy{font-size:11px;font-weight:600;fill:var(--green);}
  .icon-ring{fill:none;stroke:var(--deep-green);stroke-width:1.4;}
  .icon-line{fill:none;stroke:var(--deep-green);stroke-width:1.6;stroke-linejoin:round;stroke-linecap:round;}
</style>
</head>
<body>

<section class="flyer-page flyer-front">
  <svg viewBox="0 0 622 880" xmlns="http://www.w3.org/2000/svg">
    <defs>
      <linearGradient id="rooftopTones" x1="0" y1="0" x2="0.2" y2="1">
        <stop offset="0" stop-color="#b9cce0"/>
        <stop offset="0.28" stop-color="#e2e4e4"/>
        <stop offset="0.34" stop-color="#e9cfa6"/>
        <stop offset="0.42" stop-color="#8d7c6a"/>
        <stop offset="0.62" stop-color="#4d5a3c"/>
        <stop offset="1" stop-color="#3a4030"/>
      </linearGradient>
      <linearGradient id="buildingTones" x1="0" y1="0" x2="0" y2="1">
        <stop offset="0" stop-color="#a9c3de"/>
        <stop offset="0.6" stop-color="#d3d8dc"/>
        <stop offset="1" stop-color="#6e6a62"/>
      </linearGradient>
      <linearGradient id="solarTones" x1="0" y1="0" x2="1" y2="1">
        <stop offset="0" stop-color="#9cc0e6"/>
        <stop offset="0.45" stop-color="#e6eef6"/>
        <stop offset="0.6" stop-color="#3f6fc0"/>
        <stop offset="1" stop-color="#1c3f86"/>
      </linearGradient>
    </defs>

    <rect width="622" height="880" fill="var(--paper)"/>
    <polygon role="img" aria-label="Foto: begrüntes Flachdach über einer Stadt im Abendlicht" points="0,0 440,0 622,85 622,540 370,700 0,255" fill="url(#rooftopTones)"/>
    <polygon points="622,540 370,700 530,880 622,880" fill="var(--charcoal)"/>

    <rect role="img" aria-label="Foto: moderne Bürogebäude" x="57" y="302" width="280" height="165" fill="url(#buildingTones)"/>
    <rect role="img" aria-label="Foto: Solarmodule vor blauem Himmel" x="57" y="483" width="280" height="164" fill="url(#solarTones)"/>

    <text class="headline-kicker" x="62" y="121">PROFESSIONELLE</text>
    <text class="headline-main" x="60" y="168">FLACHDACH-</text>
    <text class="headline-main" x="60" y="216">LÖSUNGEN</text>
    <text class="headline-sub" x="61" y="245">Planung | Ausführung | Qualität</text>

    <text class="brand-name" x="530" y="742" text-anchor="middle">Steilhang- und</text>
    <text class="brand-name" x="530" y="762" text-anchor="middle">Kieselwerk GmbH</text>

    <text class="section-title" x="56" y="711">Über uns</text>
    <rect x="57" y="723" width="40" height="2" fill="var(--charcoal)"/>
    <text class="body-copy">
      <tspan x="57" y="758">Ein erfahrenes Unternehmen im Bereich Flachdachbau</tspan>
      <tspan x="57" y="776">mit Fokus auf hochwertige, moderne Lösungen. Wir legen</tspan>
      <tspan x="57" y="794">großen Wert auf eine enge Zusammenarbeit mit unseren</tspan>
      <tspan x="57" y="812">Kunden für optimale Ergebnisse.</tspan>
    </text>

    <rect x="57" y="848" width="15" height="15" rx="2" fill="var(--deep-green)"/>
    <path d="M61 851 q0 8 8 9 l1-2.5 -2.5-1.5 -1.5 1.5 q-2.5-1 -3-3.5 l1.5-1.5 -1.5-2.5z" fill="#fff"/>
    <text class="contact-line" x="82" y="861">06134-5520-0</text>
    <circle cx="202" cy="855" r="7.5" fill="var(--deep-green)"/>
    <g class="icon-line" style="stroke:#fff;stroke-width:1">
      <circle cx="202" cy="855" r="4.8"/>
      <ellipse cx="202" cy="855" rx="2" ry="4.8"/>
      <path d="M197.2 855 h9.6"/>
    </g>
    <text class="contact-line" x="220" y="861">www.skw-dach.de</text>
  </svg>
</section>

<section class="flyer-page flyer-back">
  <svg viewBox="0 0 622 880" xmlns="http://www.w3.org/2000/svg">
    <defs>
      <linearGradient id="dormerTones" x1="0" y1="0" x2="1" y2="1">
        <stop offset="0" stop-color="#2a2a2a"/>
        <stop offset="0.5" stop-color="#3d3f3d"/>
        <stop offset="0.8" stop-color="#7d7d78"/>
        <stop offset="1" stop-color="#b9b9b2"/>
      </linearGradient>
    </defs>
    <rect width="622" height="880" fill="var(--paper)"/>

    <text class="services-title" x="191" y="66" text-anchor="middle">Unsere</text>
    <text class="services-title" x="191" y="101" text-anchor="middle">Leistungen</text>

    <rect x="366" y="32" width="12" height="12" fill="var(--green)"/>
    <text class="brand-name-green" x="385" y="45">Steilhang- und</text>
    <text class="brand-name-green" x="385" y="65">Kieselwerk GmbH</text>

    <rect x="47" y="135" width="288" height="560" rx="14" fill="var(--panel)"/>
    <line x1="190" y1="165" x2="190" y2="405" stroke="#cfcfcf"/>
    <line x1="70" y1="286" x2="310" y2="286" stroke="#cfcfcf"/>

    <circle class="icon-ring" cx="119" cy="200" r="31"/>
    <g class="icon-line"><path d="M104 203 l15-13 15 13"/><path d="M108 200 v14 h22 v-14"/><rect x="115" y="205" width="8" height="9"/><path d="M126 190 l6-6 3 3 -6 6"/></g>
    <circle class="icon-ring" cx="255" cy="200" r="31"/>
    <g class="icon-line"><path d="M239 204 l16-15 16 15"/><path d="M243 201 v14 h24 v-14"/><path d="M248 214 v-6 M252 214 v-6 M256 214 v-6 M260 214 v-6 M264 214 v-6"/><path d="M255 184 v-6"/></g>
    <text class="service-label" x="119" y="260" text-anchor="middle">Dachsanierungen</text>
    <text class="service-label" x="255" y="260" text-anchor="middle">Wärmedämmung</text>

    <circle class="icon-ring" cx="119" cy="341" r="31"/>
    <g class="icon-line"><rect x="104" y="338" width="30" height="15"/><path d="M104 345 h30 M114 338 v15 M124 338 v15"/><circle cx="119" cy="328" r="4"/><path d="M119 353 v6"/></g>
    <circle class="icon-ring" cx="255" cy="341" r="31"/>
    <g class="icon-line"><circle cx="255" cy="341" r="13"/><path d="M242 341 h26 M255 328 v26"/><path d="M238 333 v16 M272 333 v16"/></g>
    <text class="service-label" x="119" y="401" text-anchor="middle">Solarinstallationen</text>
    <text class="service-label" x="255" y="401" text-anchor="middle">Spenglerei</text>

    <polygon role="img" aria-label="Foto: dunkle Dachgauben mit Schieferverkleidung" points="0,490 193,455 333,520 333,620 622,670 622,880 0,880" fill="url(#dormerTones)"/>

    <text class="side-title" x="374" y="151">Unsere Vorteile</text>
    <g fill="var(--bullet)">
      <circle cx="381" cy="183" r="7"/><circle cx="381" cy="220" r="7"/><circle cx="381" cy="257" r="7"/><circle cx="381" cy="312" r="7"/><circle cx="381" cy="367" r="7"/>
    </g>
    <text class="side-copy">
      <tspan x="402" y="187">Individuelle Planung nach Bedarf</tspan>
      <tspan x="402" y="224">Hochwertige Materialien</tspan>
      <tspan x="402" y="261">Fachgerechte &amp; termingerechte</tspan>
      <tspan x="402" y="279">Ausführung</tspan>
      <tspan x="402" y="316">Lösungen für kleine und große</tspan>
      <tspan x="402" y="334">Projekte</tspan>
      <tspan x="402" y="371">Erfahrenes und kompetentes Team</tspan>
    </text>

    <text class="side-title" x="374" y="428">KONTAKT</text>
    <text class="side-copy"><tspan x="374" y="449">Wir beraten Sie gerne individuell zu Ihrem</tspan><tspan x="374" y="465">Projekt.</tspan></text>
    <text class="offer-copy">
      <tspan x="374" y="487">Aktion: kostenfreie Dachinspektion</tspan>
      <tspan x="374" y="503">bis 30.06.2026 – anrufen oder Mail</tspan>
      <tspan x="374" y="519">mit Betreff „Dachinspektion 2026“.</tspan>
    </text>

    <circle cx="382" cy="541" r="9" fill="var(--deep-green)"/>
    <path d="M378 537 q0 8 8 9 l1-2.5 -2.5-1.5 -1.5 1.5 q-2.5-1 -3-3.5 l1.5-1.5 -1.5-2.5z" fill="#fff"/>
    <text class="side-copy" x="404" y="545">06134-5520-0</text>
    <circle cx="382" cy="567" r="9" fill="var(--deep-green)"/>
    <g class="icon-line" style="stroke:#fff;stroke-width:1"><rect x="376.5" y="563" width="11" height="8"/><path d="M376.5 563 l5.5 4.5 5.5-4.5"/></g>
    <text class="side-copy" x="404" y="571">info@skw-dach.de</text>
    <circle cx="382" cy="593" r="9" fill="var(--deep-green)"/>
    <g class="icon-line" style="stroke:#fff;stroke-width:1"><circle cx="382" cy="593" r="5.5"/><ellipse cx="382" cy="593" rx="2.2" ry="5.5"/><path d="M376.5 593 h11"/></g>
    <text class="side-copy" x="404" y="597">www.skw-dach.de</text>
  </svg>
</section>

</body>
</html>
```